Birchford Realty Business Card

Business Card:

Somewhere on front of card, please include Broker License Number: 5839162

Website is BirchfordRealty.example

Address is:
7218 Crestover Ave E
Saginaw, MI 48271

I'll let you use creative freedom on the rest; we obviously need Name, Title, Email (@BirchfordRealty.example), Office Phone, Cell Phone.

Don't want any special die-cutting, just a standard size business card.

On the back, include a place for the date and time of an appointment to be written in pen.

Requirements
Must have
• Our logo, attached to email.

```html
<!DOCTYPE html>
<html lang="en">
<head>
<meta charset="utf-8">
<title>Birchford Realty Business Card</title>
<link href="https://fonts.googleapis.com/css2?family=Open+Sans:wght@400;700&family=Crimson+Text:wght@400;600&display=swap" rel="stylesheet">
<style>
  :root {
    --backdrop: #e9e9e9;
    --paper: #ffffff;
    --red: #e2262b;
    --orange: #e27a26;
    --charcoal: #38383b;
    --silver: #c9c9cb;
    --navy: #23285f;
    --link-blue: #1c1ccf;
    --ink: #111111;
    --watermark: rgba(35, 40, 95, 0.12);
  }
  * { box-sizing: border-box; margin: 0; padding: 0; }
  html, body { width: 1200px; height: 784px; overflow: hidden; }
  body {
    background: var(--backdrop);
    position: relative;
    font-family: "Open Sans", Arial, sans-serif;
  }
  .card {
    position: absolute;
    top: 237px;
    width: 540px;
    height: 310px;
    background: var(--paper);
    overflow: hidden;
    box-shadow: 0 4px 14px rgba(0,0,0,0.18);
  }
  .card-back { left: 40px; font-family: "Crimson Text", Georgia, serif; color: var(--ink); }
  .card-front { left: 620px; }
  .card-shapes { position: absolute; inset: 0; width: 100%; height: 100%; }

  /* Front */
  .license {
    position: absolute; top: 14px; right: 22px;
    color: var(--link-blue); font-size: 14px;
  }
  .license .license-no { font-size: 11px; }
  .brand-name {
    position: absolute; top: 120px; left: 235px;
    font-size: 34px; font-weight: 700; color: var(--navy);
    letter-spacing: -0.5px;
  }
  .address {
    position: absolute; top: 182px; left: 300px;
    font-size: 18px; line-height: 1.3; color: var(--ink);
  }
  .website {
    position: absolute; bottom: 18px; right: 22px;
    font-size: 16px; color: var(--link-blue);
  }

  /* Back */
  .watermark {
    position: absolute; top: 150px; left: 60px;
    font-family: "Open Sans", Arial, sans-serif;
    font-size: 64px; font-weight: 700; color: var(--watermark);
    transform: rotate(-14deg); transform-origin: left center;
    white-space: nowrap;
  }
  .appointment-title {
    position: absolute; top: 14px; left: 0; width: 300px;
    text-align: center; font-size: 26px; font-weight: 600;
  }
  .form { position: absolute; top: 70px; left: 28px; right: 28px; }
  .form-row { display: flex; gap: 16px; height: 30px; align-items: flex-end; }
  .field { display: flex; flex: 1; align-items: flex-end; font-size: 19px; }
  .field-line { flex: 1; border-bottom: 2px dotted var(--ink); margin: 0 0 6px 6px; }
  .days {
    position: absolute; left: 28px; right: 28px; bottom: 14px;
    display: flex; justify-content: space-between;
  }
  .day { display: flex; flex-direction: column; align-items: center; width: 64px; }
  .day-name { font-size: 12px; margin-bottom: 4px; }
  .day-box { width: 22px; height: 22px; border: 2px solid var(--ink); }
</style>
</head>
<body>

<section class="card card-back" aria-label="Appointment card, back">
  <svg class="card-shapes" viewBox="0 0 540 310" aria-hidden="true">
    <defs>
      <linearGradient id="backBand" x1="0" x2="1" y1="0" y2="0">
        <stop offset="0" stop-color="var(--red)"/>
        <stop offset="1" stop-color="var(--orange)"/>
      </linearGradient>
    </defs>
    <path d="M0 0 H360 Q220 35 0 62 Z" fill="url(#backBand)"/>
    <path d="M300 0 H420 Q470 20 540 70 V95 Q450 35 300 0 Z" fill="var(--orange)"/>
    <path d="M540 95 Q450 35 330 20 Q450 60 540 140 Z" fill="var(--charcoal)"/>
    <path d="M540 140 Q460 75 360 45 Q460 100 540 185 Z" fill="var(--silver)"/>
  </svg>
  <div class="watermark">Birchford Realty</div>
  <h1 class="appointment-title">Appointment</h1>
  <div class="form">
    <div class="form-row"><div class="field">Name<span class="field-line"></span></div></div>
    <div class="form-row"><div class="field">Title<span class="field-line"></span></div></div>
    <div class="form-row">
      <div class="field">E-mail<span class="field-line"></span></div>
      <div class="field">Mobile-No<span class="field-line"></span></div>
    </div>
    <div class="form-row">
      <div class="field">Office-No<span class="field-line"></span></div>
      <div class="field">Time<span class="field-line"></span></div>
    </div>
    <div class="form-row"><div class="field">Date<span class="field-line"></span></div></div>
  </div>
  <div class="days">
    <div class="day"><span class="day-name">Monday</span><span class="day-box"></span></div>
    <div class="day"><span class="day-name">Tuesday</span><span class="day-box"></span></div>
    <div class="day"><span class="day-name">Wednesday</span><span class="day-box"></span></div>
    <div class="day"><span class="day-name">Thursday</span><span class="day-box"></span></div>
    <div class="day"><span class="day-name">Friday</span><span class="day-box"></span></div>
    <div class="day"><span class="day-name">Saturday</span><span class="day-box"></span></div>
    <div class="day"><span class="day-name">Sunday</span><span class="day-box"></span></div>
  </div>
</section>

<section class="card card-front" aria-label="Business card, front">
  <svg class="card-shapes" viewBox="0 0 540 310" aria-hidden="true">
    <defs>
      <linearGradient id="frontBand" x1="0" x2="1" y1="0" y2="0">
        <stop offset="0" stop-color="var(--orange)"/>
        <stop offset="1" stop-color="var(--red)"/>
      </linearGradient>
      <linearGradient id="charcoalFade" x1="0" x2="1" y1="1" y2="0">
        <stop offset="0" stop-color="#2c2c2e"/>
        <stop offset="1" stop-color="#5a5a5d"/>
      </linearGradient>
    </defs>
    <path d="M0 0 H540 V88 Q360 40 170 58 Q70 70 0 105 Z" fill="url(#frontBand)"/>
    <path d="M200 56 Q70 110 20 310 H0 V270 Q30 120 200 56 Z" fill="var(--orange)"/>
    <path d="M235 88 Q110 160 80 310 H20 Q60 150 235 88 Z" fill="url(#charcoalFade)"/>
    <path d="M255 105 Q160 180 150 310 H80 Q110 165 255 105 Z" fill="var(--silver)"/>
  </svg>
  <p class="license">License Number: <span class="license-no">5839162</span></p>
  <p class="brand-name">Birchford Realty</p>
  <address class="address" style="font-style: normal;">
    7218 Crestover Ave E<br>
    Saginaw, MI 48271
  </address>
  <p class="website">www.BirchfordRealty.example</p>
</section>

</body>
</html>
```